label for a line of bbq rubs. my competition team name is copper kettle bbq *

i already have a logo, just need a label designed for a line of bbq rubs im developing. i want the design to be clean and eye catching and my colors of my logo are black and white. these will be sold in bbq specialty stores. i have a lot of traction in the bbq competition community, they are all familiar with my logo, just need a design that will stand out and draw attention to buys online and in the stores

Target Market(s)

backyard bbq cooks

Industry/Entity Type

Food blog

Font styles to use
Sans Serif

Colors

Designer to choose only greyscale colors for use in the design.

Requirements
Must have
• project must be simple, clean, with a classic look
Nice to have
• my logo, clean and simple

i have include some examples from other companies
Should not have
• cartoons

```html
<!DOCTYPE html>
<html lang="en">
<head>
<meta charset="utf-8">
<title>Copper Kettle BBQ – Barbeque Rub Labels</title>
<link rel="stylesheet" href="https://fonts.googleapis.com/css2?family=Archivo+Black&family=Oswald:wght@400;600;700&family=Libre+Baskerville:wght@700&family=Arimo:wght@400;700&display=swap">
<style>
  :root {
    --ink: #0b0b0b;
    --paper: #ffffff;
    --stage: #ffffff;
    --mist: #e9e9e9;
    --rule: #bdbdbd;
    --shade: #5a5a5a;
  }
  * { box-sizing: border-box; margin: 0; padding: 0; }
  html, body { width: 1200px; height: 800px; overflow: hidden; background: var(--stage); }
  .sheet { position: relative; width: 1200px; height: 800px; }

  .label {
    position: absolute; width: 524px; height: 330px;
    background: var(--ink); color: var(--paper);
  }
  .label--chicken { left: 61px;  top: 60px; }
  .label--brisket { left: 615px; top: 60px; }
  .label--pig     { left: 61px;  top: 420px; }
  .label--ribs    { left: 615px; top: 420px; }

  .logo-tab {
    position: absolute; left: 198px; top: -18px; width: 124px; height: 98px;
    background: var(--paper); border-radius: 6px;
    display: flex; flex-direction: column; align-items: center; justify-content: center;
    font-family: "Archivo Black", sans-serif; color: var(--ink); text-align: center;
  }
  .logo-tab__name { font-size: 11px; line-height: 1.1; letter-spacing: .3px; }
  .logo-tab__bbq { font-size: 34px; line-height: 1; }

  .emblem {
    position: absolute; left: 40px; top: 42px; width: 66px; height: 42px;
    background: linear-gradient(180deg, var(--mist), #bfbfbf); border-radius: 20px 20px 4px 4px;
  }
  .story {
    position: absolute; left: 34px; top: 112px; width: 112px;
    font-family: "Libre Baskerville", serif; font-size: 5.6px; line-height: 1.95;
    text-align: center;
  }
  .quote-mark {
    position: absolute; font-family: "Libre Baskerville", serif; font-size: 26px; line-height: 1;
  }
  .quote-mark--open { left: 20px; top: 106px; }
  .quote-mark--close { left: 146px; top: 230px; }
  .follow {
    position: absolute; left: 44px; top: 288px;
    font-family: "Oswald", sans-serif; font-size: 9px; letter-spacing: .4px;
    display: flex; align-items: center; gap: 5px;
  }
  .follow__dot { width: 8px; height: 8px; border-radius: 50%; background: var(--paper); }

  .product {
    position: absolute; left: 160px; width: 200px; text-align: center;
    font-family: "Oswald", sans-serif;
  }
  .product__kicker { top: 104px; font-size: 22px; font-weight: 700; letter-spacing: 1px;
    text-shadow: 2px 2px 0 var(--shade); }
  .product__title { top: 108px; font-size: 40px; font-weight: 700; letter-spacing: 2px; line-height: 1;
    text-shadow: 3px 3px 0 var(--shade); }
  .product__title--big { top: 128px; font-size: 52px; }
  .product__type { top: 160px; font-size: 19px; font-weight: 400; letter-spacing: 1px; }
  .product__type--low { top: 186px; }

  .silhouette {
    position: absolute; left: 215px; top: 200px; width: 90px; height: 72px;
    background: linear-gradient(180deg, var(--paper), var(--mist)); border-radius: 40% 40% 12% 12%;
  }
  .silhouette--wide { left: 205px; top: 222px; width: 112px; height: 52px; border-radius: 45%; }
  .silhouette--low { top: 232px; height: 46px; }

  .volume-rule { position: absolute; left: 176px; top: 297px; width: 168px; height: 1px; background: var(--rule); }
  .volume { position: absolute; left: 176px; top: 304px; width: 168px; text-align: center;
    font-family: "Oswald", sans-serif; font-size: 9px; }

  .facts {
    position: absolute; left: 384px; top: 56px; width: 112px;
    background: var(--paper); color: var(--ink); padding: 3px 4px;
    font-family: "Arimo", sans-serif; font-size: 5px; line-height: 1.35;
  }
  .facts__head { font-size: 10px; font-weight: 400; border-bottom: .6px solid var(--ink); line-height: 1.2; }
  .facts__row { display: flex; justify-content: space-between; border-bottom: .4px solid var(--ink); }
  .facts__row--thick { border-bottom: 2.5px solid var(--ink); }
  .facts__row--indent { padding-left: 6px; }
  .facts__cal { font-size: 8px; font-weight: 700; display: flex; justify-content: space-between; align-items: baseline;
    border-bottom: 1.5px solid var(--ink); }
  .facts__cal b { font-size: 11px; }
  .facts__note { font-size: 3.6px; line-height: 1.3; padding-top: 2px; }
</style>
</head>
<body>
<main class="sheet">

  <!-- Chicken -->
  <section class="label label--chicken">
    <div class="logo-tab"><span class="logo-tab__name">COPPER KETTLE</span><span class="logo-tab__bbq">BBQ</span></div>
    <div class="emblem" role="img" aria-label="Emblem of a cow and a chicken"></div>
    <span class="quote-mark quote-mark--open">“</span>
    <p class="story">Lorem ipsum dolor sit amet, consectetuer adipiscing elit, sed diam nonummy nibh euismod tincidunt ut laoreet dolore magna aliquam erat volutpat. Ut wisi enim ad minim veniam, quis nostrud exerci tation ullamcorper suscipit lobortis nisl ut aliquip ex ea commodo consequat. Duis autem vel eum iriure dolor in hendrerit in vulputate velit esse molestie consequat, vel illum dolore eu feugiat nulla facilisis at vero eros</p>
    <span class="quote-mark quote-mark--close">”</span>
    <div class="follow">FOLLOW US ON <span class="follow__dot"></span></div>
    <h2 class="product product__title">CHICKEN</h2>
    <p class="product product__type">BARBEQUE RUB</p>
    <div class="silhouette" role="img" aria-label="White silhouette of a chicken"></div>
    <div class="volume-rule"></div><p class="volume">250ml</p>
    <div class="facts">
      <div class="facts__head">Nutrition Facts</div>
      <div>1 serving per container</div>
      <div class="facts__row facts__row--thick"><span>Serving size</span><span>1/4 cup (40g)</span></div>
      <div>Amount per serving</div>
      <div class="facts__cal"><span>Calories</span><b>120</b></div>
      <div class="facts__row"><span></span><span>% Daily Value*</span></div>
      <div class="facts__row"><span>Total Fat 0g</span><span>0%</span></div>
      <div class="facts__row facts__row--indent"><span>Saturated Fat 0g</span><span>0%</span></div>
      <div class="facts__row facts__row--indent"><span>Trans Fat 0g</span><span></span></div>
      <div class="facts__row"><span>Cholesterol 0mg</span><span>0%</span></div>
      <div class="facts__row"><span>Sodium 10mg</span><span>0%</span></div>
      <div class="facts__row"><span>Total Carbohydrate 32g</span><span>12%</span></div>
      <div class="facts__row facts__row--indent"><span>Dietary Fiber 2g</span><span>7%</span></div>
      <div class="facts__row facts__row--indent"><span>Total Sugars</span><span>26g</span></div>
      <div class="facts__row facts__row--indent"><span>Includes 0 Added Sugars</span><span>0%</span></div>
      <div class="facts__row facts__row--thick"><span>Protein 1g</span><span></span></div>
      <div class="facts__row"><span>Vitamin D 0mcg</span><span>0%</span></div>
      <div class="facts__row"><span>Calcium 25mg</span><span>2%</span></div>
      <div class="facts__row"><span>Iron 0.7mg</span><span>4%</span></div>
      <div class="facts__row facts__row--thick"><span>Potassium 298mg</span><span>6%</span></div>
      <p class="facts__note">* The % Daily Value (DV) tells you how much a nutrient in a serving of food contributes to a daily diet. 2,000 calories a day is used for general nutrition advice.<br><b>Ingredients: Kettle Spice Blend</b></p>
    </div>
  </section>

  <!-- Brisket -->
  <section class="label label--brisket">
    <div class="logo-tab"><span class="logo-tab__name">COPPER KETTLE</span><span class="logo-tab__bbq">BBQ</span></div>
    <div class="emblem" role="img" aria-label="Emblem of a cow and a chicken"></div>
    <span class="quote-mark quote-mark--open">“</span>
    <p class="story">Lorem ipsum dolor sit amet, consectetuer adipiscing elit, sed diam nonummy nibh euismod tincidunt ut laoreet dolore magna aliquam erat volutpat. Ut wisi enim ad minim veniam, quis nostrud exerci tation ullamcorper suscipit lobortis nisl ut aliquip ex ea commodo consequat. Duis autem vel eum iriure dolor in hendrerit in vulputate velit esse molestie consequat, vel illum dolore eu feugiat nulla facilisis at vero eros</p>
    <span class="quote-mark quote-mark--close">”</span>
    <div class="follow">FOLLOW US ON <span class="follow__dot"></span></div>
    <h2 class="product product__title">BRISKET</h2>
    <p class="product product__type">BARBEQUE RUB</p>
    <div class="silhouette silhouette--wide" role="img" aria-label="White silhouette of a cow"></div>
    <div class="volume-rule"></div><p class="volume">250ml</p>
    <div class="facts">
      <div class="facts__head">Nutrition Facts</div>
      <div>1 serving per container</div>
      <div class="facts__row facts__row--thick"><span>Serving size</span><span>1/4 cup (40g)</span></div>
      <div>Amount per serving</div>
      <div class="facts__cal"><span>Calories</span><b>120</b></div>
      <div class="facts__row"><span></span><span>% Daily Value*</span></div>
      <div class="facts__row"><span>Total Fat 0g</span><span>0%</span></div>
      <div class="facts__row facts__row--indent"><span>Saturated Fat 0g</span><span>0%</span></div>
      <div class="facts__row facts__row--indent"><span>Trans Fat 0g</span><span></span></div>
      <div class="facts__row"><span>Cholesterol 0mg</span><span>0%</span></div>
      <div class="facts__row"><span>Sodium 10mg</span><span>0%</span></div>
      <div class="facts__row"><span>Total Carbohydrate 32g</span><span>12%</span></div>
      <div class="facts__row facts__row--indent"><span>Dietary Fiber 2g</span><span>7%</span></div>
      <div class="facts__row facts__row--indent"><span>Total Sugars</span><span>26g</span></div>
      <div class="facts__row facts__row--indent"><span>Includes 0 Added Sugars</span><span>0%</span></div>
      <div class="facts__row facts__row--thick"><span>Protein 1g</span><span></span></div>
      <div class="facts__row"><span>Vitamin D 0mcg</span><span>0%</span></div>
      <div class="facts__row"><span>Calcium 25mg</span><span>2%</span></div>
      <div class="facts__row"><span>Iron 0.7mg</span><span>4%</span></div>
      <div class="facts__row facts__row--thick"><span>Potassium 298mg</span><span>6%</span></div>
      <p class="facts__note">* The % Daily Value (DV) tells you how much a nutrient in a serving of food contributes to a daily diet. 2,000 calories a day is used for general nutrition advice.<br><b>Ingredients: Kettle Spice Blend</b></p>
    </div>
  </section>

  <!-- Pig -->
  <section class="label label--pig">
    <div class="logo-tab"><span class="logo-tab__name">COPPER KETTLE</span><span class="logo-tab__bbq">BBQ</span></div>
    <div class="emblem" role="img" aria-label="Emblem of a cow and a chicken"></div>
    <span class="quote-mark quote-mark--open">“</span>
    <p class="story">Lorem ipsum dolor sit amet, consectetuer adipiscing elit, sed diam nonummy nibh euismod tincidunt ut laoreet dolore magna aliquam erat volutpat. Ut wisi enim ad minim veniam, quis nostrud exerci tation ullamcorper suscipit lobortis nisl ut aliquip ex ea commodo consequat. Duis autem vel eum iriure dolor in hendrerit in vulputate velit esse molestie consequat, vel illum dolore eu feugiat nulla facilisis at vero eros</p>
    <span class="quote-mark quote-mark--close">”</span>
    <div class="follow">FOLLOW US ON <span class="follow__dot"></span></div>
    <h2 class="product product__title product__title--big" style="top:118px">PIG</h2>
    <p class="product product__type product__type--low">BARBEQUE RUB</p>
    <div class="silhouette silhouette--wide silhouette--low" role="img" aria-label="White silhouette of a pig"></div>
    <div class="volume-rule"></div><p class="volume">250ml</p>
    <div class="facts">
      <div class="facts__head">Nutrition Facts</div>
      <div>1 serving per container</div>
      <div class="facts__row facts__row--thick"><span>Serving size</span><span>1/4 cup (40g)</span></div>
      <div>Amount per serving</div>
      <div class="facts__cal"><span>Calories</span><b>120</b></div>
      <div class="facts__row"><span></span><span>% Daily Value*</span></div>
      <div class="facts__row"><span>Total Fat 0g</span><span>0%</span></div>
      <div class="facts__row facts__row--indent"><span>Saturated Fat 0g</span><span>0%</span></div>
      <div class="facts__row facts__row--indent"><span>Trans Fat 0g</span><span></span></div>
      <div class="facts__row"><span>Cholesterol 0mg</span><span>0%</span></div>
      <div class="facts__row"><span>Sodium 10mg</span><span>0%</span></div>
      <div class="facts__row"><span>Total Carbohydrate 32g</span><span>12%</span></div>
      <div class="facts__row facts__row--indent"><span>Dietary Fiber 2g</span><span>7%</span></div>
      <div class="facts__row facts__row--indent"><span>Total Sugars</span><span>26g</span></div>
      <div class="facts__row facts__row--indent"><span>Includes 0 Added Sugars</span><span>0%</span></div>
      <div class="facts__row facts__row--thick"><span>Protein 1g</span><span></span></div>
      <div class="facts__row"><span>Vitamin D 0mcg</span><span>0%</span></div>
      <div class="facts__row"><span>Calcium 25mg</span><span>2%</span></div>
      <div class="facts__row"><span>Iron 0.7mg</span><span>4%</span></div>
      <div class="facts__row facts__row--thick"><span>Potassium 298mg</span><span>6%</span></div>
      <p class="facts__note">* The % Daily Value (DV) tells you how much a nutrient in a serving of food contributes to a daily diet. 2,000 calories a day is used for general nutrition advice.<br><b>Ingredients: Kettle Spice Blend</b></p>
    </div>
  </section>

  <!-- Backyard Ribs -->
  <section class="label label--ribs">
    <div class="logo-tab"><span class="logo-tab__name">COPPER KETTLE</span><span class="logo-tab__bbq">BBQ</span></div>
    <div class="emblem" role="img" aria-label="Emblem of a cow and a chicken"></div>
    <span class="quote-mark quote-mark--open">“</span>
    <p class="story">Lorem ipsum dolor sit amet, consectetuer adipiscing elit, sed diam nonummy nibh euismod tincidunt ut laoreet dolore magna aliquam erat volutpat. Ut wisi enim ad minim veniam, quis nostrud exerci tation ullamcorper suscipit lobortis nisl ut aliquip ex ea commodo consequat. Duis autem vel eum iriure dolor in hendrerit in vulputate velit esse molestie consequat, vel illum dolore eu feugiat nulla facilisis at vero eros</p>
    <span class="quote-mark quote-mark--close">”</span>
    <div class="follow">FOLLOW US ON <span class="follow__dot"></span></div>
    <p class="product product__kicker">BACKYARD</p>
    <h2 class="product product__title product__title--big" style="top:128px">RIBS</h2>
    <p class="product product__type product__type--low">BARBEQUE RUB</p>
    <div class="silhouette silhouette--wide silhouette--low" role="img" aria-label="White silhouette of a pig"></div>
    <div class="volume-rule"></div><p class="volume">250ml</p>
    <div class="facts">
      <div class="facts__head">Nutrition Facts</div>
      <div>1 serving per container</div>
      <div class="facts__row facts__row--thick"><span>Serving size</span><span>1/4 cup (40g)</span></div>
      <div>Amount per serving</div>
      <div class="facts__cal"><span>Calories</span><b>120</b></div>
      <div class="facts__row"><span></span><span>% Daily Value*</span></div>
      <div class="facts__row"><span>Total Fat 0g</span><span>0%</span></div>
      <div class="facts__row facts__row--indent"><span>Saturated Fat 0g</span><span>0%</span></div>
      <div class="facts__row facts__row--indent"><span>Trans Fat 0g</span><span></span></div>
      <div class="facts__row"><span>Cholesterol 0mg</span><span>0%</span></div>
      <div class="facts__row"><span>Sodium 10mg</span><span>0%</span></div>
      <div class="facts__row"><span>Total Carbohydrate 32g</span><span>12%</span></div>
      <div class="facts__row facts__row--indent"><span>Dietary Fiber 2g</span><span>7%</span></div>
      <div class="facts__row facts__row--indent"><span>Total Sugars</span><span>26g</span></div>
      <div class="facts__row facts__row--indent"><span>Includes 0 Added Sugars</span><span>0%</span></div>
      <div class="facts__row facts__row--thick"><span>Protein 1g</span><span></span></div>
      <div class="facts__row"><span>Vitamin D 0mcg</span><span>0%</span></div>
      <div class="facts__row"><span>Calcium 25mg</span><span>2%</span></div>
      <div class="facts__row"><span>Iron 0.7mg</span><span>4%</span></div>
      <div class="facts__row facts__row--thick"><span>Potassium 298mg</span><span>6%</span></div>
      <p class="facts__note">* The % Daily Value (DV) tells you how much a nutrient in a serving of food contributes to a daily diet. 2,000 calories a day is used for general nutrition advice.<br><b>Ingredients: Kettle Spice Blend</b></p>
    </div>
  </section>

</main>
</body>
</html>
```